Barrister in Western Australia needs a fully custom logo, stationery and fonts

Barrister based in Western Australia seeking a fully custom logo, electronic and hardcopy stationery set (including email signature, document headers and footers for use with retainer agreement, invoices, letters of advice etc), custom fonts and business card design. Certain non-optional wording regarding liability limitation has to appear on documents (wording will be supplied but is on the uploaded examples). Have used this platform previously and have outgrown the previous design - samples of which are attached. I live very close to, and spend a significant amount time when not working in or around, the ocean. Use of colours or designs representative of that would be appreciated. The final design should try and communicate strength (of representation), the ability to be flexible (for example, settlements) and the fact I make myself accessible to clients - all factors shown in water/ocean.

Target Market(s)

Legal services providers, solicitors

Industry/Entity Type

Legal

Font styles to use
Serif
Decorative

Requirements
Must have
• Certain insurance wording regarding limitation of liability. Progressive feel to the set including a custom font for use in Office 365. Logo or design that is progressive - can relate to the ocean, water or waves (representing an ability to be fluid, dynamic but inheerent strength)
Nice to have
• Colour
Should not have
• Traditional calligraphy or legal fonts or feel - should not contain any traditional legal industry designs such as pens, scales of justice etc.

```html
<!DOCTYPE html>
<html lang="en">
<head>
<meta charset="UTF-8">
<title>Harriet L Moreland — Barrister Stationery</title>
<link rel="stylesheet" href="https://fonts.googleapis.com/css2?family=Outfit:wght@600&family=Source+Sans+3:wght@400&display=swap">
<style>
  :root {
    --ink: #2b3135;
    --teal: #0089aa;
    --wash: #e4f1f5;
    --card-bg: #f1f5f6;
    --sheet-edge: #e2e6e8;
    --page-bg: #ffffff;
  }
  * { margin: 0; padding: 0; box-sizing: border-box; }
  html, body {
    width: 1200px; height: 1200px; overflow: hidden;
    background: var(--page-bg);
  }
  .canvas { position: relative; width: 1200px; height: 1200px; }

  .letterhead {
    position: absolute; left: 164px; top: 130px;
    width: 669px; height: 948px;
    background: #fff;
    border: 1px solid var(--sheet-edge);
    overflow: hidden;
  }
  .watermark-area {
    position: absolute; left: 0; top: 380px;
    width: 669px; height: 490px;
    background:
      radial-gradient(ellipse 60% 55% at 82% 40%, var(--wash) 0%, rgba(228,241,245,0.7) 55%, rgba(228,241,245,0) 100%),
      radial-gradient(ellipse 75% 35% at 45% 82%, var(--wash) 0%, rgba(228,241,245,0.6) 50%, rgba(228,241,245,0) 100%);
  }
  .brand {
    position: absolute; text-align: center;
    font-family: "Outfit", sans-serif; color: var(--ink);
  }
  .brand-mark {
    display: block; margin: 0 auto; border-radius: 50%;
    background: var(--teal);
  }
  .brand-name { font-weight: 600; letter-spacing: -0.02em; line-height: 1; white-space: nowrap; }
  .brand-role { font-weight: 600; line-height: 1; white-space: nowrap; }

  .letterhead .brand { left: 34px; top: 46px; width: 220px; }
  .letterhead .brand-mark { width: 34px; height: 34px; margin-bottom: 22px; }
  .letterhead .brand-name { font-size: 21px; }
  .letterhead .brand-role { font-size: 11px; letter-spacing: 0.33em; margin-top: 5px; padding-left: 0.33em; }

  .contact-rule {
    position: absolute; left: 58px; top: 781px;
    width: 113px; height: 2px; background: var(--teal);
  }
  .contact, .disclaimer {
    position: absolute; left: 58px;
    font-family: "Source Sans 3", sans-serif; color: var(--ink);
  }
  .contact { top: 792px; font-size: 9.5px; line-height: 12px; list-style: none; }
  .contact .label { display: inline-block; width: 13px; }
  .disclaimer { top: 848px; width: 352px; font-size: 8.8px; line-height: 10.9px; }
  .footer-band {
    position: absolute; left: 0; right: 0; bottom: 2px;
    height: 22px; background: var(--teal);
  }

  .business-card {
    position: absolute; left: 633px; top: 234px;
    width: 425px; height: 244px;
    background: var(--card-bg);
    border: 1px solid var(--sheet-edge);
  }
  .business-card .brand { left: 0; right: 0; top: 28px; }
  .business-card .brand-mark { width: 48px; height: 48px; margin-bottom: 36px; }
  .business-card .brand-name { font-size: 31px; }
  .business-card .brand-role { font-size: 16px; letter-spacing: 0.36em; margin-top: 8px; padding-left: 0.36em; }
  .card-notice {
    position: absolute; left: 0; right: 0; top: 207px; text-align: center;
    font-family: "Source Sans 3", sans-serif; font-size: 8px; color: var(--ink);
  }
</style>
</head>
<body>
<main class="canvas">
  <section class="letterhead">
    <div class="watermark-area" role="img" aria-label="Large faint ocean wave decoration in pale teal"></div>
    <header class="brand">
      <span class="brand-mark"></span>
      <div class="brand-name">Harriet L Moreland</div>
      <div class="brand-role">BARRISTER</div>
    </header>

    <div class="contact-rule"></div>
    <ul class="contact">
      <li><span class="label">m.</span>+61 (0) 400 123 456</li>
      <li><span class="label">t.</span>+61 8 9000 1234</li>
      <li><span class="label">a.</span>Level 8, 15 Harbour Quay, Perth, WA, 6000</li>
    </ul>
    <p class="disclaimer">Disclaimer: Liability limited by a scheme approved under Professional Standards Legislation. This email (including any attachments) is confidential and may be privileged. It may be read, copied and used only by the intended recipient. If you have received it in error, please contact the sender immediately by return email. Please then delete both emails and do not disclose their contents to any person.</p>
    <div class="footer-band"></div>
  </section>

  <section class="business-card">
    <header class="brand">
      <span class="brand-mark"></span>
      <div class="brand-name">Harriet L Moreland</div>
      <div class="brand-role">BARRISTER</div>
    </header>
    <p class="card-notice">Liability limited by a scheme approved under Professional Standards Legislation.</p>
  </section>
</main>
</body>
</html>
```